Need Edgy Web Design Home Page for Entertainment Agency

We need a web design splash page for our entertainment company, Vexa Prime Agency based (Los Angeles and New York).
Vexa Prime is a full service PR, marketing and special events agency based in Los Angeles and New York. We aim to serve the most elite in entertainment, media and sports.

With a combined experience of over 30 years in the entertainment industry, our team is committed to deliver each client with the upmost service and contemporary strategies to increase your business objective.

CREATIVE, EDGY & TRENDSETTING

SERVICES

PR Campaigns

Media Relations

Talent Representation

Brand Marketing & Activations

Special Events: Publicity & Consulting

EXPERTISE

Television

Film

Talent

Music

Marketing & Promotions

Industry Events

Digital & Social Media

Looking for a home page that is flashy, edgy and creative. I've provided our logos and contact details:

Delia Fortunez
dfortunez@kelvoritla.com

Tobias Renn
trenn@kelvoritny.com

Paloma Quiroga
pquiroga@kelvoritla.com

Target Market(s)

Los Angeles and New York

Industry/Entity Type

Entertainment

Number of Pages Required

1 page

Font styles to use
Serif
Decorative

Requirements
Must have
• 1. Logo
• 2. Description of services but done creatively
• 4. Visuals (Stock images: cool edgy millennials & graphics images that make sense for our agency)
• 5. Contact Details
• Reference: https://www.tunelathery.net & http://www.thevolrenagency.com
Nice to have
• If possible would love to have stock cartoon images included as images of Delia and I. Reference image (http://www.pixmerrow.com/pic-482915306/stock-vector-cute-cartoon-characters-young-boy-and-girl-in-cool-casual-outfits.html)
Should not have
• Should not look boring!

```html
<!DOCTYPE html>
<html lang="en">
<head>
<meta charset="utf-8">
<title>Vexa Prime — Entertainment Agency</title>
<link rel="stylesheet" href="https://fonts.googleapis.com/css2?family=Abel&family=Bitter:wght@400;700&family=Lato:ital,wght@0,400;0,700;1,400&family=Quicksand:wght@400;500&display=swap">
<style>
:root{
  --gold:#c9bd55;
  --gold-text:#d9c874;
  --ink:#0b0b0b;
  --night-top:#070a1c;
  --night-mid:#0f1a45;
  --night-low:#1c2d70;
  --white:#ffffff;
  --body-text:#2c2c2c;
  --tagline:#2a2a55;
  --pr-green:#6aa479;
  --media-yellow:#e9b53e;
  --talent-teal:#5aa6a8;
  --brand-red:#e0503a;
  --events-blue:#1b58b6;
  --title-green:#7fc08a;
  --title-yellow:#f0b93e;
  --title-teal:#6cc1c1;
  --title-red:#f05a3c;
  --title-blue:#3d8af0;
}
*{box-sizing:border-box;margin:0;padding:0}
html,body{width:1200px;height:2612px;overflow:hidden}
body{background:var(--gold);font-family:'Lato',sans-serif;color:var(--body-text)}
.page{position:relative;width:1200px;height:2612px;overflow:hidden;background:var(--gold)}
.abs{position:absolute}

/* masthead */
.masthead{left:0;top:55px;width:1200px;height:115px;background:var(--ink);clip-path:polygon(0 8px,100% 0,100% 100%,0 100%)}
.brand{left:100px;top:92px;display:flex;align-items:center;gap:12px}
.brand-dot{width:44px;height:44px;border-radius:50%;background:var(--gold-text)}
.brand-name{font-family:'Bitter',serif;font-size:28px;color:var(--gold-text);font-weight:400;line-height:1;white-space:nowrap}
.phone{right:94px;top:16px;display:flex;align-items:center;gap:10px;font-size:22px;color:var(--ink)}
.main-nav{top:114px;left:0;width:1200px}
.main-nav a{position:absolute;font-family:'Abel',sans-serif;font-size:17px;color:#e8e8e8;text-decoration:none;letter-spacing:.3px}
.main-nav a.active{color:var(--gold-text)}
.main-nav a.active::after{content:"";position:absolute;left:0;right:0;top:26px;height:2px;background:var(--gold-text)}

/* hero */
.hero{left:0;top:150px;width:1200px;height:610px;background:radial-gradient(ellipse at 60% 20%,#b88a5a 0%,#6b4a30 30%,#2a1c14 65%,#0e0a08 100%);clip-path:polygon(0 15px,100% 8px,100% 477px,0 608px)}
.hero-caption{left:0;width:1200px;top:485px;text-align:center}
.hero-caption span{display:inline-block;background:rgba(30,26,24,.72);padding:6px 12px;font-family:'Bitter',serif;font-size:30px;color:#fff;letter-spacing:1px}
.hero-arrow{top:461px;width:32px;height:32px;border-radius:50%;background:rgba(0,0,0,.7);display:flex;align-items:center;justify-content:center}

/* welcome */
.welcome{left:0;top:600px;width:1200px;height:480px;background:var(--white);clip-path:polygon(0 0,100% 0,100% 340px,0 471px)}
.welcome-title{left:169px;top:766px;font-family:'Bitter',serif;font-weight:400;font-size:38px;color:#1e1e1e;letter-spacing:.5px}
.tagline{left:169px;top:815px;width:650px;font-style:italic;font-size:15.5px;line-height:23px;color:var(--tagline)}
.intro{left:169px;top:872px;width:640px;font-size:14px;line-height:22.5px;color:var(--body-text)}
.duo{left:871px;top:723px;width:165px;height:210px;background:linear-gradient(160deg,#e7d7c7,#b7a48a 55%,#6a5a40);border-radius:14px;opacity:.85}

/* services */
.services{left:0;top:900px;width:1200px;height:610px;background:radial-gradient(ellipse at 50% 100%,var(--night-low) 0%,var(--night-mid) 45%,var(--night-top) 100%);clip-path:polygon(0 171px,100% 40px,100% 514px,0 607px)}
.service{display:flex;gap:14px;width:340px}
.service-icon{flex:0 0 105px;width:105px;height:105px;border-radius:50%;border:3px solid rgba(255,255,255,.85);display:flex;align-items:center;justify-content:center}
.service-icon.pr{background:var(--pr-green)}
.service-icon.media{background:var(--media-yellow)}
.service-icon.talent{background:var(--talent-teal)}
.service-icon.brand{background:var(--brand-red)}
.service-icon.events{background:var(--events-blue)}
.service-body{padding-top:8px}
.service h3{font-family:'Bitter',serif;font-weight:400;font-size:18px;line-height:23px;margin-bottom:4px}
.service p{font-size:13px;line-height:19px;color:#e6e7f2}
.service .more{display:block;margin-top:10px;font-size:12.5px;color:#e6e7f2;letter-spacing:.3px}
.pr h3{color:var(--title-green)}
.media h3{color:var(--title-yellow)}
.talent h3{color:var(--title-teal)}
.brandmk h3{color:var(--title-red)}
.events h3{color:var(--title-blue)}

/* expertise */
.expertise-title{left:95px;top:1536px;font-family:'Bitter',serif;font-size:30px;font-weight:400;color:#1b1b1b;letter-spacing:.5px}
.view-all{left:1019px;top:1545px;font-family:'Abel',sans-serif;font-size:16px;color:#1b1b1b;text-decoration:underline}
.tile{width:242px;height:187px;overflow:hidden}
.tile-label{position:absolute;left:0;right:0;bottom:0;height:34px;background:rgba(20,20,20,.55);color:#fff;font-size:19.5px;text-align:center;line-height:34px}
.grid-arrow{top:1785px}

/* footer */
.footer{left:0;top:2070px;width:1200px;height:460px;background:radial-gradient(ellipse at 50% 100%,var(--night-low) 0%,var(--night-mid) 40%,var(--night-top) 100%);clip-path:polygon(0 8px,100% 70px,100% 425px,0 447px)}
.footer-brand{left:968px;top:2112px;display:flex;align-items:center;gap:12px}
.footer-brand .brand-dot{width:60px;height:60px;background:var(--ink);border:3px solid var(--gold-text)}
.footer-brand .brand-name{font-size:20px;margin-top:22px}
.footer-nav{left:0;top:2158px;width:1200px}
.footer-nav a{position:absolute;font-family:'Abel',sans-serif;font-size:16px;color:#e8e8e8;text-decoration:none}
.footer-nav a.active{color:var(--gold-text)}
.col-title{font-family:'Quicksand',sans-serif;font-size:25px;color:#f0f0f0;font-weight:400;border-bottom:1px solid rgba(255,255,255,.18);padding-bottom:8px}
.divider{top:2245px;width:1px;height:200px;background:rgba(255,255,255,.18)}
.contact-line{display:flex;gap:12px;align-items:flex-start;color:#e6e7f2;font-size:12.5px;line-height:19px}
.contact-line strong{font-weight:700}
.person{font-size:13px;line-height:18px;color:#e6e7f2}
.person strong{display:block;font-weight:700;color:#f4f4f4}
.social{display:flex;gap:8px;align-items:center;font-size:13px;color:#e6e7f2}
.social i{display:block;width:20px;height:20px;background:var(--gold-text)}
.thumb{width:105px;height:82px}
.more-link{left:742px;top:2485px;font-size:12px;color:var(--gold-text)}
.copyright{left:127px;top:2565px;font-size:13px;color:#1b1b1b;font-weight:700}
</style>
</head>
<body>
<div class="page">

  <!-- masthead -->
  <div class="abs masthead"></div>
  <div class="abs brand"><span class="brand-dot"></span><span class="brand-name">Vexa Prime</span></div>
  <div class="abs phone">
    <svg width="26" height="26" viewBox="0 0 26 26"><circle cx="13" cy="13" r="11.5" fill="none" stroke="#0b0b0b" stroke-width="2"/><path d="M9 7.5c.8-.6 1.6-.4 2 .4l1 1.9c.3.7.1 1.2-.5 1.6l-.6.4c.6 1.5 1.8 2.8 3.3 3.5l.5-.6c.5-.6 1-.7 1.6-.4l1.9 1.1c.8.4.9 1.2.3 1.9-1.2 1.4-3 1.3-4.9.1-2.6-1.6-4.5-4.2-4.8-6.5-.2-1.3.2-2.7.9-3.4z" fill="#0b0b0b"/></svg>
    1-555-04172
  </div>
  <nav class="abs main-nav">
    <a class="active" style="left:606px">HOME</a>
    <a style="left:679px">ABOUT US</a>
    <a style="left:782px">OUR SERVICES</a>
    <a style="left:915px">EXPERTISE</a>
    <a style="left:1024px">CONTACT US</a>
  </nav>

  <!-- hero & welcome backgrounds -->
  <div class="abs welcome"></div>
  <div class="abs hero" role="img" aria-label="Concert crowd with raised hands under warm stage lights"></div>
  <div class="abs services" role="img" aria-label="Deep blue starry night sky backdrop"></div>

  <div class="abs hero-caption"><span>EVERY EVENTS SHOULD BE PERFECT</span></div>
  <div class="abs hero-arrow" style="left:31px"><svg width="12" height="14" viewBox="0 0 12 14"><path d="M9 1 3 7l6 6" fill="none" stroke="#fff" stroke-width="2"/></svg></div>
  <div class="abs hero-arrow" style="left:1142px"><svg width="12" height="14" viewBox="0 0 12 14"><path d="M3 1l6 6-6 6" fill="none" stroke="#fff" stroke-width="2"/></svg></div>

  <!-- welcome -->
  <h1 class="abs welcome-title">WELCOME TO VEXA PRIME</h1>
  <p class="abs tagline">Vexa Prime is a full service PR, marketing and special events agency based in Los Angeles.<br>We aim to serve the most elite in entertainment, media and sports.</p>
  <p class="abs intro">With a combined experience of over 30 years in the entertainment industry, our team is committed to deliver each client with the upmost service and contemporary strategies to increase your business objective.</p>
  <div class="abs duo" role="img" aria-label="Cartoon illustration of two young agency founders in casual outfits"></div>

  <!-- services -->
  <div class="abs service pr" style="left:94px;top:1103px">
    <div class="service-icon pr"><svg width="56" height="50" viewBox="0 0 56 50"><path d="M6 18h10l24-12v36L16 30H6z" fill="#fff"/><path d="M12 30l4 14h7l-4-14z" fill="#fff"/><path d="M45 15c4 4 4 14 0 18M49 10c7 7 7 21 0 28" fill="none" stroke="#fff" stroke-width="3" stroke-linecap="round"/></svg></div>
    <div class="service-body"><h3>PR Campaigns</h3><p>Aliquam vitae magna aliquet, molestie est eget, ultricies arcu. Nunc non luctus turpis.</p><span class="more">MORE INFO</span></div>
  </div>
  <div class="abs service media" style="left:442px;top:1103px">
    <div class="service-icon media"><svg width="56" height="56" viewBox="0 0 56 56"><g fill="#fff"><rect x="9" y="10" width="11" height="16" rx="5.5"/><rect x="22.5" y="6" width="11" height="16" rx="5.5"/><rect x="36" y="10" width="11" height="16" rx="5.5"/><rect x="13" y="26" width="3" height="22"/><rect x="26.5" y="22" width="3" height="26"/><rect x="40" y="26" width="3" height="22"/></g></svg></div>
    <div class="service-body"><h3>Media Relations</h3><p>Aliquam vitae magna aliquet, molestie est eget, ultricies arcu. Nunc non luctus turpis.</p><span class="more">MORE INFO</span></div>
  </div>
  <div class="abs service talent" style="left:793px;top:1103px">
    <div class="service-icon talent"><svg width="60" height="48" viewBox="0 0 60 48"><g fill="#fff"><circle cx="14" cy="14" r="6"/><circle cx="30" cy="10" r="7"/><circle cx="46" cy="14" r="6"/><path d="M4 38c0-8 4-14 10-14s10 6 10 14z"/><path d="M18 38c0-10 5-17 12-17s12 7 12 17z"/><path d="M36 38c0-8 4-14 10-14s10 6 10 14z"/><rect x="2" y="38" width="56" height="4"/></g></svg></div>
    <div class="service-body"><h3>Talent Representation</h3><p>Aliquam vitae magna aliquet, molestie est eget, ultricies arcu. Nunc non luctus turpis.</p><span class="more">MORE INFO</span></div>
  </div>
  <div class="abs service brandmk" style="left:270px;top:1270px">
    <div class="service-icon brand"><svg width="58" height="52" viewBox="0 0 58 52"><g fill="#fff"><rect x="6" y="36" width="8" height="12"/><rect x="18" y="30" width="8" height="18"/><rect x="30" y="22" width="8" height="26"/><rect x="42" y="14" width="8" height="34"/></g><path d="M4 30 L40 6" stroke="#fff" stroke-width="4" stroke-linecap="round"/><path d="M34 3h12v12z" fill="#fff"/></svg></div>
    <div class="service-body"><h3>Brand Marketing &amp;<br>Activations</h3><p>Aliquam vitae magna aliquet, molestie est eget, ultricies arcu. Nunc non luctus turpis.</p><span class="more">MORE INFO</span></div>
  </div>
  <div class="abs service events" style="left:618px;top:1270px">
    <div class="service-icon events"><svg width="54" height="54" viewBox="0 0 54 54"><rect x="6" y="10" width="42" height="38" rx="4" fill="none" stroke="#fff" stroke-width="4"/><rect x="6" y="10" width="42" height="9" fill="#fff"/><rect x="15" y="4" width="4" height="11" rx="2" fill="#fff"/><rect x="35" y="4" width="4" height="11" rx="2" fill="#fff"/><rect x="25" y="24" width="4" height="13" rx="2" fill="#fff"/><circle cx="27" cy="42" r="2.4" fill="#fff"/></svg></div>
    <div class="service-body"><h3>Special Events: Publicity<br>&amp; Consulting</h3><p>Aliquam vitae magna aliquet, molestie est eget, ultricies arcu. Nunc non luctus turpis.</p><span class="more">MORE INFO</span></div>
  </div>

  <!-- expertise -->
  <h2 class="abs expertise-title">EXPERTISE</h2>
  <span class="abs view-all">VIEW ALL ››</span>
  <svg class="abs grid-arrow" style="left:44px" width="20" height="36" viewBox="0 0 20 36"><path d="M17 2 3 18l14 16" fill="none" stroke="#4a4628" stroke-width="4"/></svg>
  <svg class="abs grid-arrow" style="left:1136px" width="20" height="36" viewBox="0 0 20 36"><path d="M3 2l14 16L3 34" fill="none" stroke="#4a4628" stroke-width="4"/></svg>

  <div class="abs tile" style="left:94px;top:1611px;background:linear-gradient(160deg,#8e9294,#4d5256 60%,#2a2d30)" role="img" aria-label="Television film crew shooting on a city street"><span class="tile-label">Television</span></div>
  <div class="abs tile" style="left:348px;top:1611px;background:linear-gradient(170deg,#7a4a2c,#3a2518 55%,#5e3a26)" role="img" aria-label="Theatre audience facing a lit stage screen"><span class="tile-label">Film</span></div>
  <div class="abs tile" style="left:606px;top:1611px;background:linear-gradient(160deg,#d9dde2,#8d8aa8 55%,#4c4a6a)" role="img" aria-label="Business team meeting around a table"><span class="tile-label">Talent</span></div>
  <div class="abs tile" style="left:862px;top:1611px;background:radial-gradient(ellipse at 50% 20%,#3e8cf0,#143a8a 55%,#050a22)" role="img" aria-label="Concert crowd under blue stage lights"><span class="tile-label">Music</span></div>
  <div class="abs tile" style="left:92px;top:1826px;background:linear-gradient(160deg,#f1f2f2,#b8bcc0 55%,#6f757a)" role="img" aria-label="Team presenting marketing ideas in an office"><span class="tile-label">Marketing &amp; Promotions</span></div>
  <div class="abs tile" style="left:347px;top:1826px;background:radial-gradient(ellipse at 50% 30%,#c9a35a,#6a2f5a 55%,#241028)" role="img" aria-label="Gala event hall with purple and gold lighting"><span class="tile-label">Industry Events</span></div>
  <div class="abs tile" style="left:606px;top:1826px;background:radial-gradient(ellipse at 50% 40%,#d28a4a,#3a2a3a 55%,#121424)" role="img" aria-label="Hands surrounded by floating app tiles"><span class="tile-label">Digital &amp; Social Media</span></div>
  <div class="abs tile" style="left:862px;top:1826px;background:linear-gradient(170deg,#d8dcd8,#5a6a4a 50%,#2c3428)" role="img" aria-label="Outdoor screening event in a garden atrium"><span class="tile-label">Film</span></div>

  <!-- footer -->
  <div class="abs footer" role="img" aria-label="Deep blue starry night sky backdrop"></div>
  <div class="abs footer-brand"><span class="brand-dot"></span><span class="brand-name">Vexa Prime</span></div>
  <nav class="abs footer-nav">
    <a class="active" style="left:125px">HOME</a>
    <a style="left:223px">ABOUT US</a>
    <a style="left:348px">OUR SERVICES</a>
    <a style="left:526px">EXPERTISE</a>
    <a style="left:679px">CONTACT US</a>
  </nav>

  <div class="abs divider" style="left:402px"></div>
  <div class="abs divider" style="left:697px"></div>

  <div class="abs" style="left:125px;top:2234px;width:245px">
    <h4 class="col-title">Contact Details</h4>
    <div class="contact-line" style="margin-top:14px">
      <svg width="14" height="20" viewBox="0 0 14 20"><path d="M7 0a7 7 0 0 1 7 7c0 5-7 13-7 13S0 12 0 7a7 7 0 0 1 7-7z" fill="#b9bccf"/><circle cx="7" cy="7" r="2.6" fill="#0f1a45"/></svg>
      <div><strong>VEXA PRIME</strong><br>Lorem ipsum dolor sit amet,<br>consectetu adipiscing elit</div>
    </div>
    <div class="contact-line" style="margin-top:14px;align-items:center;font-size:17px">
      <svg width="16" height="16" viewBox="0 0 16 16"><path d="M3 1c1-.6 1.8-.3 2.2.5l1 2c.3.7.1 1.2-.5 1.6l-.7.4c.7 1.7 2 3 3.6 3.7l.5-.7c.5-.6 1-.7 1.7-.4l2 1.1c.8.4.9 1.3.3 2.1-1.4 1.600-3.4 1.4-5.4.2C4.8 10 2.8 7.3 2.4 4.8 2.1 3.3 2.3 1.7 3 1z" fill="#b9bccf"/></svg>
      1-555-04172
    </div>
    <div class="contact-line" style="margin-top:14px;align-items:center">
      <svg width="18" height="13" viewBox="0 0 18 13"><rect x=".5" y=".5" width="17" height="12" fill="none" stroke="#b9bccf"/><path d="M1 1l8 6 8-6" fill="none" stroke="#b9bccf"/></svg>
      info@vexaprime.com
    </div>
  </div>

  <div class="abs" style="left:435px;top:2234px;width:240px">
    <h4 class="col-title">Contact Persons</h4>
    <div style="display:flex;gap:22px;margin-top:14px">
      <p class="person"><strong>Tobias Renn</strong>President</p>
      <p class="person"><strong>Delia Fortunez</strong>President</p>
    </div>
    <p class="person" style="margin-top:10px"><strong>Paloma Quiroga</strong>Partner &amp; Legal Counsel</p>
    <div style="display:flex;gap:26px;margin-top:20px">
      <span class="social"><i></i>@VexaPrimeLA</span>
      <span class="social"><i></i>@VexaPrimeLA</span>
    </div>
    <span class="social" style="margin-top:12px"><i></i>@VexaPrimeLA</span>
  </div>

  <div class="abs" style="left:740px;top:2234px;width:345px">
    <h4 class="col-title">Photo Gallery</h4>
  </div>
  <div class="abs thumb" style="left:742px;top:2299px;background:linear-gradient(170deg,#6a5a8a,#2a2238)" role="img" aria-label="Event hall with stage lighting"></div>
  <div class="abs thumb" style="left:862px;top:2299px;background:linear-gradient(170deg,#4a8ad0,#16305a)" role="img" aria-label="Conference with large screens"></div>
  <div class="abs thumb" style="left:982px;top:2299px;background:linear-gradient(170deg,#d07a3a,#5a2814)" role="img" aria-label="Banquet room in warm light"></div>
  <div class="abs thumb" style="left:742px;top:2395px;background:linear-gradient(170deg,#d8c89a,#5a6a3a)" role="img" aria-label="Outdoor garden reception"></div>
  <div class="abs thumb" style="left:862px;top:2395px;background:linear-gradient(170deg,#3a3a44,#0e0e14)" role="img" aria-label="Press wall backdrop at a premiere"></div>
  <div class="abs thumb" style="left:982px;top:2395px;background:linear-gradient(170deg,#eeeeea,#9a9a90)" role="img" aria-label="Wedding ceremony aisle"></div>
  <span class="abs more-link">More +</span>

  <p class="abs copyright">Copyright © 2015 VEXA PRIME. All Rights Reserved.</p>
</div>
</body>
</html>
```